Design The Quillbrook Hompage

See powerpoint

Industry/Entity Type

SAAS data product

Coding

Coded - Design and coding required

Number of Pages Required

4 page

Font styles to use
Sans Serif

```html
<!DOCTYPE html>
<html lang="en">
<head>
<meta charset="utf-8">
<title>The Quillbrook – Public Data Made Easy</title>
<link href="https://fonts.googleapis.com/css2?family=Figtree:wght@300;400;500;600;700;800&display=swap" rel="stylesheet">
<style>
:root{
  --blue:#0a7cf0;
  --blue-soft:#9fcbf5;
  --orange:#f78b0c;
  --ink:#0d0d12;
  --text:#1d1d24;
  --footer-a:#eaf3fd;
  --footer-b:#d7ecfb;
  --line:#c9d3dd;
}
*{box-sizing:border-box;margin:0;padding:0}
html,body{width:804px;height:1200px;overflow:hidden;background:#fff}
body{font-family:"Figtree",sans-serif;color:var(--text);position:relative}
.abs{position:absolute}

/* Navigation */
.nav{position:absolute;left:0;top:0;width:804px;height:47px;background:#fff;border-bottom:1px solid #d4d9df;z-index:3}
.brand{position:absolute;display:flex;align-items:center;gap:6px;font-weight:800;color:var(--ink)}
.brand-dot{border-radius:50%;background:var(--blue)}
.nav .brand{left:86px;top:12px;font-size:17px}
.nav .brand-dot{width:18px;height:18px}
.menu a{position:absolute;top:17px;font-size:10px;color:var(--ink);text-decoration:none}
.menu .active:after{content:"";position:absolute;left:-4px;right:-4px;top:28px;height:2px;background:var(--orange)}
.btn{position:absolute;color:#fff;font-weight:800;font-size:10px;display:flex;align-items:center;justify-content:center;border-radius:1px}
.btn-signup{left:589px;top:12px;width:75px;height:24px;background:var(--orange)}
.btn-login{left:671px;top:12px;width:75px;height:24px;background:var(--blue)}

/* Hero */
.hero{position:absolute;left:0;top:47px;width:804px;height:445px}
.hero-title{position:absolute;left:67px;top:84px;font-size:35px;line-height:41px;color:var(--ink)}
.hero-title .light{font-weight:300;display:block}
.hero-title .bold{font-weight:800;display:inline-block;position:relative}
.hero-title .bold:after{content:"";position:absolute;left:2px;right:2px;bottom:4px;height:3px;background:var(--blue);z-index:-1}
.hero-copy{position:absolute;left:67px;width:245px;font-size:10.4px;line-height:11.8px;color:var(--text)}
.cta{position:absolute;left:67px;top:275px;width:171px;height:31px;background:var(--blue);color:#fff;font-weight:700;font-size:10.5px;display:flex;align-items:center;justify-content:center;gap:5px;border-radius:1px}
.photo{position:absolute;left:399px;top:76px;width:318px;height:284px;border-radius:28px;background:linear-gradient(135deg,#e8ebee 0%,#cfd6dd 45%,#7f95b4 75%,#3f5a85 100%)}
.card-mini{position:absolute;background:#fff;border-radius:6px;box-shadow:0 2px 8px rgba(40,90,150,.12)}

/* Features */
.features-title{position:absolute;left:0;width:804px;top:542px;text-align:center;font-size:23px;font-weight:800;color:var(--ink)}
.features-rule{position:absolute;left:359px;top:574px;width:120px;height:3px;background:var(--blue)}
.features-sub{position:absolute;left:100px;width:604px;top:584px;text-align:center;font-size:16px;line-height:18.5px;color:var(--text)}
.feature{position:absolute;background:#fff;border:1.5px solid var(--blue-soft);border-radius:12px;text-align:center}
.feature.focus{border-color:var(--orange);border-bottom-width:5px}
.feature h3{position:absolute;left:0;right:0;font-size:14.5px;font-weight:800;color:var(--ink)}
.feature p{position:absolute;left:24px;right:24px;font-size:10px;line-height:11.2px;color:var(--text)}
.icon-disc{position:absolute;width:64px;height:64px;border-radius:50%;background:var(--blue);display:flex;align-items:center;justify-content:center}
.pager span{position:absolute;top:937px;height:2px;width:53px;background:var(--blue-soft)}
.pager .on{background:var(--blue)}

/* Footer */
.footer{position:absolute;left:0;top:977px;width:804px;height:223px;background:linear-gradient(100deg,var(--footer-a) 0%,#e6f1fc 60%,var(--footer-b) 100%)}
.footer .brand{left:66px;top:44px;font-size:18px}
.footer .brand-dot{width:20px;height:20px}
.footer-about{position:absolute;left:76px;top:95px;width:160px;font-size:8px;line-height:10.8px}
.social{position:absolute;top:140px;font-size:8px;font-weight:700;color:var(--blue)}
.col h4{position:absolute;font-size:11px;font-weight:800;color:var(--ink)}
.col a{position:absolute;font-size:7.4px;color:var(--ink);text-decoration:none}
.footer-rule{position:absolute;left:56px;top:183px;width:722px;height:1px;background:var(--line)}
.copyright{position:absolute;left:0;width:804px;top:195px;text-align:center;font-size:8.4px}
</style>
</head>
<body>

<header class="nav">
  <div class="brand"><span class="brand-dot"></span>The Quillbrook</div>
  <nav class="menu">
    <a class="active" style="left:272px">Home</a>
    <a style="left:331px">Pricing</a>
    <a style="left:395px">Documentation</a>
    <a style="left:497px">Data</a>
    <a style="left:550px">Blog</a>
  </nav>
  <div class="btn btn-signup">Sign Up</div>
  <div class="btn btn-login">Login</div>
</header>

<section class="hero">
  <svg class="abs" style="left:0;top:0" width="804" height="445" viewBox="0 0 804 445">
    <defs>
      <linearGradient id="heroBg" x1="0" y1="0" x2="1" y2="1">
        <stop offset="0" stop-color="#b5d9fb"/>
        <stop offset=".55" stop-color="#dcefff"/>
        <stop offset="1" stop-color="#a9ecf8"/>
      </linearGradient>
    </defs>
    <path d="M0 0H804V400C720 440 600 445 450 436C300 425 150 405 0 436Z" fill="url(#heroBg)"/>
  </svg>

  <h1 class="hero-title"><span class="light">Public Data</span><span class="bold">Made Easy</span></h1>
  <p class="hero-copy" style="top:175px">From demographics to economics, from weather to health, on country level or community level. The Quillbrook collects many public data sources and organizes it for you.</p>
  <p class="hero-copy" style="top:234px;width:256px">Use The Quillbrook API or SDK to easily get public data from many different sources.</p>
  <div class="cta">Register &amp; Start for Free
    <svg width="15" height="9" viewBox="0 0 15 9"><path d="M0 4.5H13M9.5 1L13.5 4.5L9.5 8" stroke="#fff" stroke-width="1.2" fill="none"/></svg>
  </div>

  <svg class="abs" style="left:440px;top:68px" width="290" height="290" viewBox="0 0 290 290">
    <path d="M20 0H260A28 28 0 0 1 288 28V252A28 28 0 0 1 260 280" stroke="var(--blue)" stroke-width="9" fill="none"/>
  </svg>
  <div class="photo" role="img" aria-label="Photo of two colleagues smiling while reviewing data on a tablet"></div>

  <div class="card-mini" style="left:375px;top:153px;width:99px;height:66px">
    <svg width="99" height="66" viewBox="0 0 99 66">
      <g fill="#29a3e6">
        <rect x="11" y="39" width="2.5" height="6"/><rect x="16" y="32" width="2.5" height="13"/><rect x="20" y="22" width="2.5" height="23"/>
        <rect x="25" y="28" width="2.5" height="17"/><rect x="29" y="25" width="2.5" height="20"/><rect x="33" y="30" width="2.5" height="15"/>
        <rect x="37" y="20" width="2.5" height="25"/><rect x="41" y="28" width="2.5" height="17"/><rect x="45" y="32" width="2.5" height="13"/>
        <rect x="49" y="26" width="2.5" height="19"/><rect x="54" y="23" width="2.5" height="22"/><rect x="58" y="31" width="2.5" height="14"/>
        <rect x="62" y="28" width="2.5" height="17"/><rect x="66" y="20" width="2.5" height="25"/><rect x="70" y="29" width="2.5" height="16"/>
        <rect x="75" y="25" width="2.5" height="20"/><rect x="79" y="31" width="2.5" height="14"/><rect x="83" y="23" width="2.5" height="22"/>
      </g>
      <path d="M9 46H89" stroke="#ccd" stroke-width=".5"/>
    </svg>
  </div>

  <div class="card-mini" style="left:683px;top:90px;width:98px;height:73px">
    <svg width="98" height="73" viewBox="0 0 98 73">
      <rect x="8" y="12" width="82" height="1.5" fill="#888"/>
      <g>
        <rect x="33" y="18" width="10" height="6" fill="#1b86d8"/><rect x="43" y="18" width="10" height="6" fill="#0a6cc4"/><rect x="53" y="18" width="10" height="6" fill="#1b86d8"/><rect x="63" y="18" width="10" height="6" fill="#0a6cc4"/>
        <rect x="33" y="24" width="10" height="6" fill="#7fc2ee"/><rect x="43" y="24" width="10" height="6" fill="#3aa1e4"/><rect x="53" y="24" width="10" height="6" fill="#a6d6f4"/><rect x="63" y="24" width="10" height="6" fill="#3aa1e4"/>
        <rect x="33" y="30" width="40" height="22" fill="#f2f7fb"/>
        <rect x="53" y="52" width="20" height="6" fill="#3aa1e4"/>
      </g>
      <rect x="78" y="18" width="2" height="30" fill="#1b86d8"/>
    </svg>
  </div>

  <div class="card-mini" style="left:635px;top:306px;width:71px;height:62px">
    <svg width="71" height="62" viewBox="0 0 71 62">
      <circle cx="27" cy="31" r="16" fill="none" stroke="#4cb6ea" stroke-width="11"/>
      <circle cx="27" cy="31" r="16" fill="none" stroke="#0e78cc" stroke-width="11" stroke-dasharray="30 100" transform="rotate(120 27 31)"/>
      <circle cx="27" cy="31" r="16" fill="none" stroke="#8fd3f5" stroke-width="11" stroke-dasharray="18 100" transform="rotate(-80 27 31)"/>
      <g fill="#3aa1e4"><rect x="54" y="26" width="2" height="2"/><rect x="54" y="30" width="2" height="2"/><rect x="54" y="34" width="2" height="2"/><rect x="54" y="38" width="2" height="2"/></g>
    </svg>
  </div>
</section>

<h2 class="features-title">Designed for developers in need of data</h2>
<div class="features-rule"></div>
<p class="features-sub">As a data scientist or engineer you always are looking for getting more data in with more efficiency. This is exactly what The Quillbrook is making possible for you</p>

<div class="feature" style="left:-20px;top:680px;width:76px;height:182px"></div>
<div class="feature" style="left:745px;top:680px;width:80px;height:182px"></div>

<div class="feature" style="left:78px;top:708px;width:206px;height:182px">
  <h3 style="top:56px">Integrate</h3>
  <p style="top:80px">Use the quillbrook API to combine Public data with your own company data and create value for your business.</p>
</div>
<div class="icon-disc" style="left:146px;top:686px">
  <svg width="36" height="36" viewBox="0 0 36 36" fill="none" stroke="#fff" stroke-width="1.4">
    <rect x="4" y="12" width="28" height="17" rx="1"/><path d="M14 33H22M18 29V33"/>
    <circle cx="18" cy="14" r="4"/><circle cx="18" cy="14" r="7" stroke-dasharray="3 2"/>
  </svg>
</div>

<div class="feature focus" style="left:297px;top:680px;width:206px;height:186px">
  <h3 style="top:44px">Many Sources</h3>
  <p style="top:68px">Public data comes from many sources, all with their own data format and interface. No longer worry about these differences, The Quillbrook collects and standardizes it for you.</p>
</div>
<div class="icon-disc" style="left:365px;top:648px">
  <svg width="36" height="36" viewBox="0 0 36 36" fill="none" stroke="#fff" stroke-width="1.4">
    <rect x="3" y="3" width="9" height="11"/><rect x="24" y="3" width="9" height="11"/>
    <rect x="3" y="22" width="9" height="11"/><rect x="24" y="22" width="9" height="11"/>
    <circle cx="18" cy="18" r="2"/><path d="M13 13L16 16M23 13L20 16M13 23L16 20M23 23L20 20"/>
  </svg>
</div>

<div class="feature" style="left:515px;top:708px;width:206px;height:182px">
  <h3 style="top:50px">Automate</h3>
  <p style="top:74px">Use the latest public data in your data pipeline as the quillbrook makes daily updates to the data. You no longer need to worry about multiple differnt data sources.</p>
</div>
<div class="icon-disc" style="left:588px;top:680px">
  <svg width="38" height="38" viewBox="0 0 38 38" fill="none" stroke="#fff" stroke-width="1.5">
    <circle cx="19" cy="19" r="5"/><circle cx="19" cy="19" r="10" stroke-dasharray="4 2.5"/>
    <path d="M6 14A14 14 0 0 1 30 8M32 24A14 14 0 0 1 8 30"/>
  </svg>
</div>

<div class="pager"><span class="on" style="left:321px"></span><span style="left:383px"></span><span style="left:441px"></span></div>

<footer class="footer">
  <div class="brand"><span class="brand-dot"></span>The Quillbrook</div>
  <p class="footer-about">The Quillbrook was created to simplify access to public data and save you countless hours of manual collection</p>
  <span class="social" style="left:77px">Chirp</span>
  <span class="social" style="left:104px">Linkup</span>

  <div class="col">
    <h4 style="left:289px;top:50px">The Quillbrook Product</h4>
    <a style="left:290px;top:70px">Introduction</a>
    <a style="left:290px;top:85px">The datamodels</a>
    <a style="left:290px;top:101px">The API</a>
    <a style="left:290px;top:116px">The SDK</a>
  </div>
  <div class="col">
    <h4 style="left:466px;top:50px">The Company</h4>
    <a style="left:467px;top:70px">About</a>
    <a style="left:467px;top:85px">Frequently Asked Questions</a>
    <a style="left:467px;top:101px">Privacy Policy</a>
    <a style="left:467px;top:116px">Cookie Policy</a>
    <a style="left:467px;top:131px">Terms of Service</a>
  </div>
  <div class="col">
    <h4 style="left:612px;top:52px">Contact us</h4>
    <svg class="abs" style="left:616px;top:74px" width="11" height="8" viewBox="0 0 11 8"><rect width="11" height="8" fill="#4a9be8"/><path d="M0 0L5.5 4.5L11 0" stroke="#fff" fill="none" stroke-width=".8"/></svg>
    <a style="left:631px;top:72px">Email: hello@quillbrook-data.io</a>
  </div>
  <div class="footer-rule"></div>
  <p class="copyright">© 2024 The Quillbrook. All rights reserved.</p>
</footer>

</body>
</html>
```